KORVEL'S BRAND-PACKAGING DESIGN FOR A CHAMOY PICKLE IN A POUCH

This is a project for Marisol Korvel from Flickora. WE ARE CREATING A PACKAGING DESIGN FOR A PICKLE IN A POUCH. OUR FIRST RELEASE WILL BE FOR A CHAMOY FLAVORED-RED PICKLE IN A POUCH. THIS IS FOR CRAZY PICKLE FLAVORS (MAINLY CHAMOY PICKLE); WE WANT THE DESIGN TO HAVE FUN AND PLAYFUL VIBE. WE WANT IT TO POP. WE LIKE VIBRANT COLORS THESE TYPES OF PICKLES ARE NORMALLY EATEN WITH CANDY (MOSTLY MEXICAN CANDY) IN THEM, WHICH IS WHAT MAKES THEM SO POPULAR AND UNIQUE.

WE WILL NEED A FRONT DESIGN AND A BACK DESIGN OF THE PICKLE POUCH.

IMAGE MEASUREMENTS ARE: 4.5 INCHES x 9 INCHES

THE ACTUAL LOOK AND SHAPE OF THE POUCH IS IN THE PHOTOS WITH THE TAPE MEASURE IN THEM.

FRONT OF PACKAGE DESIGN:
TEAR LINE ONE INCH FROM TOP: PLEASE SEE PHOTOS

BACK OF PACKAGE DESIGN:
LEAVE EXTRA ROOM ON THE BACK DESIGN. IT WILL HAVE A BARCODE ON IT AS WELL AS A QR CODE, NUTRITION LABEL ,INGREDIENTS AND COMPANY INFO WHICH WE WILL ADD LATER.

Font styles to use
Other font styles liked:
• bubble letters, something fun

Colors
FFF300
FFF600
FEFA6F
FFFEC7
FFFEE8
EB3D1F
EC4F4E
F09395
F8D3D4
FCEDEE
E54698
E96AAD
F1A4CE
F9D9EA
FCEFF6

Requirements
Must have
• bright colors, not pastle colors. we want the same vibe as the yum pepa tamarind candy (photos attached)
Nice to have
• Can you include some designs with a cartoon character of Marisol Korvel's face (photos attached) on the packaging? Maybe of her holding a red pickle with pickle juice dripping from it; you can look at her flick ora as well: @m_korvel

```html
<!DOCTYPE html>
<html lang="en">
<head>
<meta charset="utf-8">
<title>Korvel's Chamoy Pickle – Pouch Front</title>
<link rel="stylesheet" href="https://fonts.googleapis.com/css2?family=Titan+One&display=swap">
<style>
  :root {
    --canvas-bg: #ffffff;
    --pouch-red: #ee0909;
    --panel-black: #050505;
    --brand-red: #eb1f1f;
    --candy-yellow: #fff300;
    --splash-yellow: #fff600;
    --pickle-green: #1a9a1f;
    --outline: #000000;
    --highlight: #ffffff;
    --juice-dark: #4a0608;
    --juice-mid: #9b121a;
  }
  html, body {
    margin: 0;
    padding: 0;
    width: 1200px;
    height: 1200px;
    overflow: hidden;
    background: var(--canvas-bg);
  }
  .canvas {
    position: relative;
    width: 1200px;
    height: 1200px;
  }
  .pouch-front {
    position: absolute;
    left: 330px;
    top: 60px;
    width: 540px;
    height: 1080px;
    background: var(--pouch-red);
    font-family: "Titan One", sans-serif;
  }
  .label-panel {
    position: absolute;
    left: 59px;
    top: 180px;
    width: 421px;
    height: 840px;
    background: var(--panel-black);
    overflow: hidden;
  }
  .pickle-photo {
    position: absolute;
    left: 0;
    top: 283px;
    width: 421px;
    height: 557px;
    border-radius: 210px 210px 0 0 / 50px 50px 0 0;
    background:
      radial-gradient(ellipse 30% 50% at 25% 40%, var(--juice-mid), transparent 70%),
      radial-gradient(ellipse 28% 50% at 78% 40%, #6e0b10, transparent 70%),
      linear-gradient(180deg, var(--juice-dark) 0%, #2a0305 70%, var(--panel-black) 100%);
  }
  .character-art {
    position: absolute;
    left: 103px;
    top: 318px;
    width: 204px;
    height: 252px;
    border-radius: 95px 95px 12px 12px;
    background: linear-gradient(180deg, #3a2a26 0%, #e9b79f 45%, #c0141b 75%, #a50f15 100%);
    box-shadow: 0 0 0 5px var(--highlight);
  }
  .brand-splash {
    position: absolute;
    left: 150px;
    top: 125px;
    width: 235px;
    height: 230px;
    border-radius: 50%;
    background: radial-gradient(circle at 50% 50%, var(--splash-yellow) 0%, var(--splash-yellow) 58%, rgba(255, 246, 0, 0) 72%);
  }
  .brand-name {
    position: absolute;
    left: 0;
    width: 540px;
    top: 200px;
    margin: 0;
    text-align: center;
    font-family: "Titan One", sans-serif;
    font-size: 100px;
    font-weight: 400;
    line-height: 1;
    color: var(--brand-red);
  }
  .tagline {
    position: absolute;
    left: 0;
    width: 540px;
    top: 405px;
    margin: 0;
    text-align: center;
    font-size: 30px;
    line-height: 1;
    color: var(--candy-yellow);
    transform: rotate(2deg);
  }
  .product-word {
    position: absolute;
    left: 0;
    width: 540px;
    margin: 0;
    text-align: center;
    line-height: 1;
    letter-spacing: 2px;
    -webkit-text-stroke: 2px var(--highlight);
    text-shadow:
      7px 0 0 var(--outline), -7px 0 0 var(--outline),
      0 7px 0 var(--outline), 0 -7px 0 var(--outline),
      5px 5px 0 var(--outline), -5px -5px 0 var(--outline),
      5px -5px 0 var(--outline), -5px 5px 0 var(--outline);
  }
  .product-word--flavor {
    top: 752px;
    font-size: 90px;
    color: var(--brand-red);
  }
  .product-word--item {
    top: 862px;
    font-size: 90px;
    color: var(--pickle-green);
  }
  .net-content {
    position: absolute;
    left: 0;
    width: 540px;
    top: 972px;
    margin: 0;
    text-align: center;
    font-size: 28px;
    line-height: 1;
    color: var(--candy-yellow);
  }
</style>
</head>
<body>
  <main class="canvas">
    <section class="pouch-front" aria-label="Chamoy pickle pouch front">
      <div class="label-panel">
        <div class="pickle-photo" role="img" aria-label="Close-up photo of a red chamoy-coated pickle"></div>
        <div class="character-art" role="img" aria-label="Cartoon illustration of the brand founder holding a red pickle"></div>
      </div>
      <div class="brand-splash" role="img" aria-label="Yellow chamoy splash decoration behind the brand name"></div>
      <h1 class="brand-name">Korvel's</h1>
      <p class="tagline">DELICIOUS FLAVORED</p>
      <p class="product-word product-word--flavor">CHAMOY</p>
      <p class="product-word product-word--item">PICKLE</p>
      <p class="net-content">Content: One Pickle</p>
    </section>
  </main>
</body>
</html>
```